I want a business card that is going to show a creative spark but without limiting me to an industry. Something edgy but that wont go out of date. I want it state My business name Serafina Loire, profession - Professional Makeup Artist contact number and email

My service is to provide makeup services from bridal, fashion, photography, film, TV and so on. It is creative and different so i want that to be reflected.

I would like the card double sided.
Updates

 I would LOVE a background on my card something like this image... i can supply an image to be formed like this

Please use the image uploaded

Can we try using the image provided on one side of the card and then writing and details on the other side

Target Market(s)

I am targeting a wide range of people from Creative directors to the individual eg. bride

Industry/Entity Type

Business

Requirements
Must have
• Name: Delphine Hartwell
contact numbe 0417853120
email address:info@serafinaloire.com
website: www.serafinaloire.com
One of the images attached

professional makeup artist / hair stylist

I want it to show creativity
Nice to have
• logo, Double-sided card
Should not have
• the design should not use tradional style. Or images that are not my own

```html
<!DOCTYPE html>
<html lang="en">
<head>
<meta charset="utf-8">
<title>Serafina Loire — Business Cards</title>
<link rel="stylesheet" href="https://fonts.googleapis.com/css2?family=Nothing+You+Could+Do&family=Open+Sans:wght@400&display=swap">
<style>
  :root {
    --page: #ffffff;
    --ink: #0a0a0a;
    --white: #ffffff;
    --cream-light: #f8e9c3;
    --cream-dark: #decb9f;
    --copper-light: #d38d5a;
    --copper-mid: #b06a34;
    --copper-dark: #6e4119;
    --script: "Nothing You Could Do", cursive;
    --sans: "Open Sans", sans-serif;
  }
  * { margin: 0; padding: 0; box-sizing: border-box; }
  html, body { width: 1200px; height: 761px; overflow: hidden; background: var(--page); }
  .sheet { position: relative; width: 1200px; height: 761px; }

  .card { position: absolute; width: 530px; height: 316px; overflow: hidden; }
  .card--tl { left: 48px; top: 43px; }
  .card--tr { left: 624px; top: 43px; }
  .card--bl { left: 48px; top: 398px; }
  .card--br { left: 624px; top: 398px; }

  .tone--cream { background: linear-gradient(90deg, var(--cream-light), var(--cream-dark)); }
  .tone--copper { background: linear-gradient(90deg, var(--copper-light), var(--copper-mid) 55%, var(--copper-dark)); }

  /* Front */
  .front .band-bottom { position: absolute; left: 0; right: 0; bottom: 0; height: 48px; background: var(--ink); }
  .front .mark { position: absolute; left: 236px; top: 52px; width: 58px; height: 58px; border-radius: 50%; background: var(--ink); }
  .front .name { position: absolute; left: 0; right: 0; top: 150px; text-align: center;
    font-family: var(--script); font-size: 40px; color: var(--ink); line-height: 1; }
  .front .role { position: absolute; left: 0; right: 0; top: 214px; text-align: center;
    font-family: var(--sans); font-size: 10px; letter-spacing: 0.3px; color: #2a2a2a; }

  /* Back */
  .back { background: var(--ink); }
  .back .band-top { position: absolute; left: 0; right: 0; top: 0; height: 45px; }
  .back .mark { position: absolute; left: 184px; top: 196px; width: 44px; height: 44px; border-radius: 50%; background: var(--white); }
  .back .details { position: absolute; right: 28px; top: 197px; text-align: right; color: var(--white); font-family: var(--sans); }
  .back .role { font-size: 11px; letter-spacing: 0.2px; }
  .back .name { font-family: var(--script); font-size: 27px; line-height: 1.1; margin: 4px 0 6px; }
  .back .line { display: flex; justify-content: flex-end; align-items: center; gap: 6px; font-size: 11px; margin-top: 5px; }
  .back .line svg { width: 13px; height: 13px; flex: none; }
</style>
</head>
<body>
<main class="sheet">

  <section class="card card--tl front tone--cream" aria-label="Card front, cream">
    <div class="mark"></div>
    <h1 class="name">Serafina Loire</h1>
    <p class="role">PROFESSIONAL MAKEUP ARTIST</p>
    <div class="band-bottom"></div>
  </section>

  <section class="card card--tr front tone--copper" aria-label="Card front, copper">
    <div class="mark"></div>
    <h1 class="name">Serafina Loire</h1>
    <p class="role">PROFESSIONAL MAKEUP ARTIST</p>
    <div class="band-bottom"></div>
  </section>

  <section class="card card--bl back" aria-label="Card back, cream">
    <div class="band-top tone--cream"></div>
    <div class="mark"></div>
    <div class="details">
      <p class="role">PROFESSIONAL MAKEUP ARTIST</p>
      <p class="name">Serafina Loire</p>
      <p class="line">
        <svg viewBox="0 0 13 13" aria-hidden="true"><rect x="2" y="0.5" width="9" height="12" rx="1" fill="none" stroke="#fff"/><rect x="3.5" y="2" width="6" height="3" fill="#fff"/><g fill="#fff"><rect x="3.5" y="6.5" width="1.6" height="1.4"/><rect x="5.7" y="6.5" width="1.6" height="1.4"/><rect x="7.9" y="6.5" width="1.6" height="1.4"/><rect x="3.5" y="9" width="1.6" height="1.4"/><rect x="5.7" y="9" width="1.6" height="1.4"/><rect x="7.9" y="9" width="1.6" height="1.4"/></g></svg>
        0417853120
      </p>
      <p class="line">
        <svg viewBox="0 0 13 13" aria-hidden="true"><rect x="0.5" y="2.5" width="12" height="8" fill="none" stroke="#fff"/><path d="M0.5 2.5 L6.5 7 L12.5 2.5" fill="none" stroke="#fff"/></svg>
        hello@serafinaloire.com.au
      </p>
    </div>
  </section>

  <section class="card card--br back" aria-label="Card back, copper">
    <div class="band-top tone--copper"></div>
    <div class="mark"></div>
    <div class="details">
      <p class="role">PROFESSIONAL MAKEUP ARTIST</p>
      <p class="name">Serafina Loire</p>
      <p class="line">
        <svg viewBox="0 0 13 13" aria-hidden="true"><rect x="2" y="0.5" width="9" height="12" rx="1" fill="none" stroke="#fff"/><rect x="3.5" y="2" width="6" height="3" fill="#fff"/><g fill="#fff"><rect x="3.5" y="6.5" width="1.6" height="1.4"/><rect x="5.7" y="6.5" width="1.6" height="1.4"/><rect x="7.9" y="6.5" width="1.6" height="1.4"/><rect x="3.5" y="9" width="1.6" height="1.4"/><rect x="5.7" y="9" width="1.6" height="1.4"/><rect x="7.9" y="9" width="1.6" height="1.4"/></g></svg>
        0417853120
      </p>
      <p class="line">
        <svg viewBox="0 0 13 13" aria-hidden="true"><rect x="0.5" y="2.5" width="12" height="8" fill="none" stroke="#fff"/><path d="M0.5 2.5 L6.5 7 L12.5 2.5" fill="none" stroke="#fff"/></svg>
        hello@serafinaloire.com.au
      </p>
    </div>
  </section>

</main>
</body>
</html>
```